Website for a financial survey consultancy

WHO WE ARE
We're a niche HR consultancy specialising in salary comparison surveys for the financial asset management industry. We position ourselves as a small, highly responsive organisation with a strong personal relationship with each of our 50+ blue-chip clients.

WHAT WE DO
Our business is 80% surveys (= products), 20% consultancy (= services). The surveys are a set of online products which clients interact with to find the information they are interested in.

WHAT WE WANT
We are completely revising our existing marketing website and need a new up-to-date look and feel for the site. We want you to design 2 web pages
- Home page
- Internal content page

More details below in Must Have Priorities.

REFERENCE SITES
- www.pellimorn.com - nice background image
- www.vantrikel.com - ignoring the animations
- www.quorvalen.com
- www.lumiscap.com - clean, fresh, styly but prob not corporate enough
- www.dorvethfunds.com - spacious, beautiful, slightly dated tho
- www.thalbin.co.uk - ignore the colours. Like the simplicity, larger font size (although want to stick with sans-serif fonts for main content)

DELIVERABLES
The final designs should be delivered as one or more PSD files with clearly named layers. All design elements and treatments should be separated out, for example use adjustment layers rather than applied (and subsequently irreversible) adjustments, strokes, shading, etc.

WHAT NEXT
I'll be monitoring the contest every day and can respond to questions fast. You can IM me on Skype or MSN.
Updates

Project Deadline Extended
Reason: Hi folks,

I am extending the deadline to this project as I am travelling this week and therefore will not be able to make a final decision until next Monday. I will try and provide further feedback over the course of this week but I am only going to be online occasionally so be prepared to wait a few days for a reply from me.

Thanks for all the designs so far.

Owen

Target Market(s)

In order of importance, most important first

1. Potential customers - UK & US financial industry HR professionals, short on time. Heard about us already, want to find out more about what we do, confirm relevance for their needs. Core goal - establish credibility: are we properly resourced, will we be around for years to come, are we *real*.

2. Existing customers - UK & US financial industry professionals, short on time, under pressure, want results quickly, minimum faff, expect high quality, slickly presented information. Primary action: login and use surveys.

3. Industry professionals/researchers - probably arriving through blog content, looking to browse and hoover information. Valuable for their ability to spread awareness of who we are amongst their peers.

Industry/Entity Type

Financial

Requirements
Must have
• GENERAL
Style cues - Corporate, professional, financial, stylish, slick, clean, spacious, light
Size - standard 960px grid

NAVIGATION
- [ Home | About us | Surveys | Consulting | Blog ]
- Sub-nav (roll-over dropdown) on About Us, Surveys & Consulting

ALL PAGES
- Site navigation
- Client login (on screen permanently or link to ajaxy in-page pop-up)
- Footer section
- Existing logo (attached)* - this is obviously an important reference point in the design, esp colour

HOME PAGE
- Communicate (link thru to?) survey/consulting split
- Large photo(s)/backdrop (2-3 interchangeable options ideally). Please consider what rights agreement will be necessary for any photos you include in your design.
- Possibly bigger more prominent version of logo
- Strap line/sentence - "Focussed data is the key to success"
- 3 recent blog posts (should look good with and without blog post images)
- Free downloadable PDF research report + supporting blurb

INTERNAL PAGE
- Page title
- Content - typical page will be less than one screenfull
- Level 1 sub-heading
- Level 2 sub-heading
- Bulleted list
- Content supporting image (any image will do - interested in placement, borders (if any), spacing, caption, etc)
- 'Do something' button

* Note: there is some internal debate about this logo at the moment. Some (me) are keen for it to change, some (not me!) are not. If you have an web page design idea/concept that requires an evolution of the logo, go ahead and evolve it. We can explore this further in the design process as necessary, but don't sweat it.
Nice to have
• Values to communicate
- Knowledgeable
- Professional
- Secure
- Personal
- Experienced
- Financial industry specific
- Accurate
- Reliable
Should not have
• - Search box
- Social media links, other than RSS feed button (discrete)

```html
<!DOCTYPE html>
<html lang="en">
<head>
<meta charset="utf-8">
<title>Corvane – HR consultancy</title>
<link rel="stylesheet" href="https://fonts.googleapis.com/css2?family=Arimo:wght@400;700&family=Archivo+Narrow:wght@400&display=swap">
<style>
  :root {
    --page-bg: #dedede;
    --brand-red: #6a0b0b;
    --nav-dark: #1c0d0d;
    --nav-red-top: #8a3a3e;
    --nav-red-bottom: #5e1c20;
    --sky-deep: #3f6598;
    --sky-light: #6f8fb8;
    --glass-pale: #c9d2d4;
    --glass-mid: #8fa3b4;
    --panel-bg: rgba(250, 248, 246, 0.94);
    --panel-edge: #c9c0b8;
    --sand: #e3d3bc;
    --sand-dark: #d6c3a6;
    --text-dark: #333333;
    --text-body: #3a3a3a;
    --white: #ffffff;
    --accent-orange: #d14a12;
    --thumb-frame: #8c8c8c;
  }
  * { margin: 0; padding: 0; box-sizing: border-box; }
  html, body { width: 1200px; height: 828px; overflow: hidden; }
  body {
    background: var(--page-bg);
    font-family: "Arimo", Arial, sans-serif;
    position: relative;
  }
  .site { position: absolute; left: 121px; top: 19px; width: 964px; height: 788px; background: var(--white); }

  /* navigation */
  .main-nav {
    position: absolute; left: 0; top: 0; width: 964px; height: 41px;
    background: linear-gradient(to bottom, var(--nav-red-top), var(--nav-red-bottom));
    display: flex;
  }
  .main-nav a {
    display: flex; align-items: center; justify-content: center;
    height: 41px; color: var(--white); text-decoration: none;
    font-weight: 700; font-size: 12px; letter-spacing: 0.2px;
    border-right: 1px solid rgba(255,255,255,0.75);
  }
  .main-nav .nav-home { width: 131px; background: var(--nav-dark); }
  .main-nav .nav-item { width: 131px; }
  .main-nav .nav-blog { width: 135px; }
  .client-login {
    position: absolute; right: 37px; top: 13px;
    color: var(--white); font-size: 12px; text-decoration: underline;
  }

  /* hero */
  .hero { position: absolute; left: 0; top: 41px; width: 964px; height: 540px; overflow: hidden; }
  .hero-backdrop {
    position: absolute; inset: 0;
    background:
      linear-gradient(105deg, transparent 0 56%, rgba(201,210,212,0.85) 62%, var(--glass-mid) 75%, var(--glass-pale) 86%, var(--glass-mid) 100%),
      linear-gradient(to bottom, var(--sky-light), var(--sky-deep) 45%, #4a72a6);
  }
  .brand-name {
    display: block; color: var(--white);
    font-weight: 700; line-height: 1; white-space: nowrap;
  }
  .hero-brand { position: absolute; left: 24px; top: 56px; font-size: 40px; }
  .hero-title {
    position: absolute; left: 20px; top: 336px;
    color: var(--white); font-weight: 400; font-size: 66px; line-height: 1; letter-spacing: -1.5px;
    transform: scaleX(0.93); transform-origin: left top; white-space: nowrap;
  }
  .hero-tagline {
    position: absolute; left: 23px; top: 404px;
    color: var(--white); font-weight: 400; font-size: 26px; line-height: 1; letter-spacing: -0.4px;
    transform: scaleX(0.91); transform-origin: left top; white-space: nowrap;
  }

  /* latest blogs */
  .blog-panel {
    position: absolute; left: 612px; top: 98px; width: 322px; height: 302px;
    background: var(--panel-bg); border: 4px solid var(--panel-edge);
    border-top-width: 2px; border-left-width: 2px;
    padding: 12px 16px 0 15px;
  }
  .blog-panel h2 {
    color: var(--brand-red); font-family: "Archivo Narrow", "Arimo", sans-serif;
    font-weight: 400; font-size: 23px; line-height: 1;
    padding-bottom: 8px; border-bottom: 5px solid var(--sand-dark);
  }
  .blog-post { margin-top: 10px; }
  .blog-post + .blog-post { margin-top: 13px; }
  .blog-post p {
    color: var(--text-dark); font-size: 11px; font-weight: 700; line-height: 13.5px;
    text-align: justify;
  }
  .read-more {
    display: inline-block; margin-top: 11px; color: #111; font-size: 11px; text-decoration: underline;
  }
  .read-arrow { color: var(--accent-orange); font-weight: 700; font-size: 12px; margin-left: 4px; }

  /* report download */
  .report-download {
    position: absolute; left: 614px; top: 438px; width: 316px; height: 50px;
    border-radius: 4px; border: 1px solid #c6ad8c;
    background: linear-gradient(to bottom, #fbf3e8, #e7d2b5);
    text-decoration: none; overflow: hidden;
  }
  .report-icon { position: absolute; left: 7px; top: 6px; width: 38px; height: 38px; background: #b31712; border-radius: 3px; }
  .report-title {
    position: absolute; left: 54px; top: 8px; color: #6b5240;
    font-family: "Archivo Narrow", "Arimo", sans-serif; font-size: 18px; line-height: 1; white-space: nowrap;
  }
  .report-sub { position: absolute; left: 55px; top: 28px; color: var(--brand-red); font-size: 12px; }

  .hero-rule { position: absolute; left: 0; top: 581px; width: 964px; height: 3px; background: var(--brand-red); }

  /* footer columns */
  .section-tab {
    position: absolute; top: 600px; width: 91px; height: 34px;
    background: var(--sand); display: flex; align-items: center; justify-content: center;
    font-size: 13px; font-weight: 700; color: #111;
  }
  .section-text { position: absolute; font-size: 11.5px; line-height: 16px; color: var(--text-body); text-align: justify; }
  .thumb {
    position: absolute; top: 660px; width: 70px; height: 70px;
    border: 3px solid var(--thumb-frame);
  }
  .thumb-surveys { left: 278px; background: linear-gradient(to bottom, #d9dde2, #9aa7b8); }
  .thumb-consulting { left: 537px; background: linear-gradient(to bottom, #c9b7a6, #e9e4de); }
  .learn-more { position: absolute; top: 751px; font-size: 12px; color: var(--brand-red); text-decoration: none; }
  .learn-more .arrow { color: #111; font-weight: 700; margin-left: 2px; }

  .footer-brand { position: absolute; left: 836px; top: 600px; font-size: 22px; }
  .footer-brand .brand-name { color: var(--brand-red); }
  .copyright { position: absolute; right: 5px; top: 767px; font-size: 11px; color: var(--brand-red); }
</style>
</head>
<body>
<div class="site">
  <nav class="main-nav">
    <a class="nav-home" href="#">HOME</a>
    <a class="nav-item" href="#">ABOUT US</a>
    <a class="nav-item" href="#">SURVEYS</a>
    <a class="nav-item" href="#">CONSULTING</a>
    <a class="nav-blog" href="#">BLOG</a>
  </nav>
  <a class="client-login" href="#">Client LOGIN</a>

  <section class="hero">
    <div class="hero-backdrop" role="img" aria-label="Blue sky with glass office tower facade rising on the right"></div>
    <div class="hero-brand">
      <span class="brand-name">Corvane</span>
    </div>
    <h1 class="hero-title">HR consultancy</h1>
    <p class="hero-tagline">Focussed data is the key to success</p>

    <aside class="blog-panel">
      <h2>Latest Blogs</h2>
      <article class="blog-post">
        <p>Lorem ipsum dolor sit amet, consectetur adipiscing elit. Integer fringilla sapien ligula. In hac habitasse platea dictumst.</p>
        <a class="read-more" href="#">Read More</a><span class="read-arrow">»</span>
      </article>
      <article class="blog-post">
        <p>Lorem ipsum dolor sit amet, consectetur adipiscing elit. Integer fringilla sapien ligula. In hac habitasse platea dictumst.</p>
        <a class="read-more" href="#">Read More</a><span class="read-arrow">»</span>
      </article>
      <article class="blog-post">
        <p>Lorem ipsum dolor sit amet, consectetur adipiscing elit. Integer fringilla sapien ligula. In hac habitasse platea dictumst.</p>
        <a class="read-more" href="#">Read More</a><span class="read-arrow">»</span>
      </article>
    </aside>

    <a class="report-download" href="#">
      <span class="report-icon"></span>
      <span class="report-title">Research Report + Supporting Blurb</span>
      <span class="report-sub">Download PDF file</span>
    </a>
  </section>
  <div class="hero-rule"></div>

  <div class="section-tab" style="left:36px">About us</div>
  <p class="section-text" style="left:36px; top:659px; width:172px">Lorem ipsum dolor sit amet, consectetur adipiscing elit. Cras ante dui, viverra non vehicula in, condimentum id ipsum. Fusce at arcu metus.</p>

  <div class="section-tab" style="left:276px">Surveys</div>
  <div class="thumb thumb-surveys" role="img" aria-label="Photo of a businessman sitting with a laptop"></div>
  <p class="section-text" style="left:358px; top:658px; width:138px; text-align:left">Lorem ipsum dolor sit amet, consectetur adipiscing elit. Cras ante dui, viverra non vehicula in, condimentum</p>
  <a class="learn-more" style="left:359px" href="#">Learn More<span class="arrow"> ››</span></a>

  <div class="section-tab" style="left:536px">Consulting</div>
  <div class="thumb thumb-consulting" role="img" aria-label="Photo of a businesswoman offering a handshake"></div>
  <p class="section-text" style="left:616px; top:658px; width:140px">Fusce at arcu metus. eu justo nisl. Maecenas con-sequat condimentum ante, quis tincidunt neque viverra sed.</p>
  <a class="learn-more" style="left:617px" href="#">Learn More<span class="arrow"> ››</span></a>

  <div class="footer-brand">
    <span class="brand-name">Corvane</span>
  </div>
  <p class="copyright">© 2011 Corvane. All rights reserved</p>
</div>
</body>
</html>
```